QuillHarbor.com Marketing Brochure

We need a brochure which can be printed but can also be sent via e-version for a new web company we have started. We are a professional writing company with a team of writers which can provide individuals/businesses with all their writing needs, such as unique blog posts, seo content, newsletters, press releases, website content, social media posts, etc. We have all the text for the brochure attached to this project, we just need the design and graphics done. we are looking for charts, graphs for the statistical information provided, we also want graphics designed which pertain to our type of business.

I have included the text required for this marketing brochure and also included our business card and logo. Brightlane LLC is the main company and Quillharbor.com is the website where clients place orders.

Industry/Entity Type

Marketing

Requirements
Must have
• tri fold brochure, both inside and outside panels utilized. want this to be easily converted to an e-version so we can email to potential clients as well. must have professionally designed graphics, our website, contact information, as well as a small address section should we choose to mail the brochure.

```html
<!DOCTYPE html>
<html lang="en">
<head>
<meta charset="utf-8">
<title>QuillHarbor.com Brochure</title>
<link href="https://fonts.googleapis.com/css2?family=Open+Sans:wght@400;700&family=Oswald:wght@400;600&family=PT+Sans+Narrow:wght@400;700&family=Tinos:wght@400;700&display=swap" rel="stylesheet">
<style>
  :root {
    --ink: #3a3a3a;
    --heading: #4a4660;
    --blue: #6f86c4;
    --plum: #524a6c;
    --lilac: #9a8fc0;
    --panel: #f1f1f1;
    --paper: #ffffff;
  }
  * { margin: 0; padding: 0; box-sizing: border-box; }
  html, body { width: 783px; height: 1200px; overflow: hidden; background: var(--paper); }
  body { font-family: "Open Sans", Arial, sans-serif; color: var(--ink); }
  .brochure { position: relative; width: 783px; height: 1200px; overflow: hidden; }

  .outside { position: absolute; left: 0; top: 0; width: 783px; height: 600px; background: var(--panel); }
  .inside { position: absolute; left: 0; top: 604px; width: 783px; height: 596px; background: var(--paper); }
  .inside-bg { position: absolute; left: 17px; top: 0; width: 750px; height: 578px; background: var(--panel); }

  /* Left outside panel */
  .intro { position: absolute; left: 40px; top: 44px; width: 214px; font-size: 7.4px; line-height: 1.18; text-align: justify; }
  .intro h3 { font-size: 8.4px; font-weight: 700; color: var(--heading); line-height: 1.1; margin-top: 8px; }
  .intro h3:first-child { margin-top: 0; }
  .intro strong { color: var(--heading); }

  /* Pricing panel */
  .pricing-head { position: absolute; left: 255px; top: 30px; width: 260px; height: 36px; background: var(--blue);
    color: #fff; font-family: "PT Sans Narrow", sans-serif; font-weight: 700; font-size: 13.5px; letter-spacing: .5px;
    text-align: center; line-height: 14px; padding-top: 4px; }
  .cost-card { position: absolute; left: 316px; top: 78px; width: 138px; height: 118px; }
  .cost-shape { position: absolute; top: 0; left: 0; }
  .cost-title { position: absolute; top: 0; left: 0; width: 138px; height: 31px; background: var(--plum); color: #fff;
    font-family: "PT Sans Narrow", sans-serif; font-size: 11.5px; text-align: center; line-height: 12px; padding-top: 4px; }
  .cost-list { position: absolute; top: 35px; left: 4px; width: 130px; text-align: center; color: #fff;
    font-family: "Tinos", serif; font-size: 11.5px; line-height: 12.8px; }

  .stats { position: absolute; left: 260px; top: 219px; width: 250px; text-align: center; font-family: "Tinos", serif;
    font-size: 8px; line-height: 1.08; color: var(--ink); }
  .stats p { margin-top: 6px; }
  .stats p:first-child { margin-top: 0; }
  .stats .num { font-family: "Oswald", sans-serif; font-weight: 600; font-size: 15px; line-height: 1; color: #222; display: block; }
  .stats .inline-num { font-family: "Oswald", sans-serif; font-weight: 600; font-size: 15px; line-height: 1; color: #222; vertical-align: -2px; }
  .stats .row { display: block; text-align: left; padding-left: 22px; line-height: 15px; }
  .web-bar { position: absolute; left: 266px; top: 543px; width: 222px; height: 24px; background: var(--blue);
    color: #fff; font-size: 13px; text-align: center; line-height: 24px; }

  /* Cover panel */
  .cover-photo { position: absolute; left: 516px; top: 17px; width: 267px; height: 450px;
    background: radial-gradient(circle at 40% 35%, #2f6f86 0%, #1b2a35 45%, #0c0f13 80%), #111; }
  .cover-photo::after { content: ""; position: absolute; inset: 0;
    background: radial-gradient(circle at 30% 25%, rgba(230,120,60,.55), transparent 35%), radial-gradient(circle at 75% 70%, rgba(210,110,60,.4), transparent 35%); }
  .quote-disc { position: absolute; left: 562px; top: 296px; width: 134px; height: 134px; border-radius: 50%;
    background: #6e6580; color: #fff; text-align: center; font-family: "Tinos", serif; padding-top: 55px; }
  .quote-disc .line { position: absolute; left: 10px; right: 10px; border-top: 1px dotted rgba(255,255,255,.6); }
  .quote-disc p { font-size: 10.5px; line-height: 12px; }
  .quote-disc cite { font-style: normal; font-weight: 700; font-size: 8px; display: block; }
  .brand { position: absolute; left: 560px; top: 540px; display: flex; align-items: center; gap: 8px; }
  .brand-dot { width: 18px; height: 18px; border-radius: 50%; background: var(--blue); }
  .brand-name { font-family: "Open Sans", sans-serif; font-weight: 700; font-size: 21px; color: var(--heading); }

  /* Inside */
  .hero-photo { position: absolute; left: 17px; top: 0; width: 227px; height: 578px;
    background: linear-gradient(180deg, #5b5b5b 0%, #3d3d3d 40%, #6c6c6c 70%, #8a8a8a 100%); }
  .hero-caption { position: absolute; left: 34px; top: 412px; width: 193px; height: 166px; background: rgba(210,210,210,.85);
    font-family: "Tinos", serif; font-size: 19px; line-height: 21px; text-align: center; color: #4c4c4c; padding-top: 30px; }
  .column { position: absolute; top: 26px; font-size: 9.3px; line-height: 1.19; text-align: justify; }
  .column h2 { font-family: "PT Sans Narrow", sans-serif; font-weight: 700; font-size: 13px; line-height: 12.5px;
    color: var(--heading); text-transform: uppercase; margin-top: 10px; text-align: left; }
  .column h2:first-child { margin-top: 0; }
  .column strong { color: var(--heading); }
  .col-mid { left: 290px; width: 216px; }
  .col-right { left: 538px; width: 228px; }
  .contact { position: absolute; left: 516px; top: 510px; width: 251px; height: 68px; background: var(--plum);
    border-top: 3px solid var(--lilac); color: #fff; font-size: 9.5px; font-weight: 700; line-height: 14px; padding: 8px 0 0 24px; }
</style>
</head>
<body>
<div class="brochure">

  <section class="outside">
    <div class="intro">
      <h3>What else can I do<br>to connect with my customers?</h3>
      <p>Newsletters are a great way to provide information to customers. The newsletter format allows multiple types of information to be conveyed at once. A mix of content types and styles – visuals and text, marketing and PR, can be delivered at once. And don't forget – a newsletter mailing list is a list of your customers and potential customers. <strong>Newsletters are another great customer engagement tool.</strong></p>
      <h3>Inbound leads are valuable</h3>
      <p>The best thing about social media and online content is that it creates another point of connection between you and your customers. They sign up for your newsletter, they follow you on Chirpline and they comment on your blog posts. Active content creates active connections with your target market. You become more attractive to your target market, and they come to you looking for a direct connection. <strong>They sign up for the right to receive your marketing messages, and they do it in droves.</strong></p>
      <h3>How can<br>QuillHarbor.com help?</h3>
      <p>Many companies outsource this type of writing. They do this for a few reasons, but the most important is writing quality. Producing high quality content on demand is a specialized skill. Our team of writers are professionals, native English speakers from the US, UK, Canada, and Australia. They can provide any kind of content you need – blog posts, social media updates, newsletters, press releases, website content, financial reports, SlideMaker presentations, and anything else you might need. <strong>We deliver high quality content to meet your needs.</strong></p>
      <h3>Get results</h3>
      <p>Your time is valuable. You make more money doing what you're best than you do writing copy. Let us write your copy – that's what we're best at. Professional copy delivers better SEO, more followers, better customer relationship management (CRM), and most importantly better financial results. <strong>We work with you to help you meet your business goals.</strong></p>
      <h3>Recap:<br>So what are the benefits?</h3>
      <p>With quality written content, your business can lower its new customer acquisition costs, expand website traffic, increase revenue per customer, optimize search engine ranking and improve ROI. <strong>Whatever your goal, QuillHarbor.com will help you get there</strong></p>
    </div>

    <div class="pricing-head">WHAT ARE YOUR<br>PRICING PACKAGES?</div>
    <div class="cost-card">
      <svg class="cost-shape" width="138" height="118" viewBox="0 0 138 118" aria-hidden="true">
        <path d="M4 28 H134 V98 L69 117 L4 98 Z" fill="var(--lilac)"/>
      </svg>
      <div class="cost-title">AVERAGE COST<br>FOR A NEW CUSTOMER</div>
      <div class="cost-list">Cold call<br>$15,000<br>Advertising<br>$13,000<br>Inbound leads<br>$5,000</div>
    </div>

    <div class="stats">
      <p><span class="num">75%</span>of Internet users never scroll past<br>the first page of search results.</p>
      <p>On Seekwell
        <span class="row"><span class="inline-num">18%</span> of clicks go to the first position</span>
        <span class="row"><span class="inline-num">10%</span> of clicks to the 2<sup>nd</sup> position and</span>
        <span class="row" style="padding-left:40px"><span class="inline-num">7%</span> to the 3<sup>rd</sup> position</span>
      </p>
      <p><span class="num">41%</span>of users never look at the second page,<br>even if the first page doesn't have what<br>they want.</p>
      <p>Organic click-through has<span class="num">25%</span>higher conversion for those intending<br>to purchase than paid click-through.</p>
      <p>An overall content marketing strategy<br>can increase revenue<span class="num">40%</span>(Halvorsen, 2012).</p>
      <p>SEO leads have a<span class="num">14.6%</span>close rate, compared with<span class="num">1.7%</span>for direct mail or print ads</p>
    </div>
    <div class="web-bar">www.quillharbor.com</div>

    <div class="cover-photo" role="img" aria-label="Close-up photo of glowing vintage typewriter keys"></div>
    <div class="quote-disc">
      <span class="line" style="top:47px"></span>
      <p>"Content is king"</p>
      <cite>Marcus Delane</cite>
      <span class="line" style="top:85px"></span>
    </div>
    <div class="brand">
      <span class="brand-dot"></span>
      <span class="brand-name">Brightlane LLC</span>
    </div>
  </section>

  <section class="inside">
    <div class="inside-bg"></div>
    <div class="hero-photo" role="img" aria-label="Photo of a child typing on a vintage typewriter"></div>
    <div class="hero-caption">Blog Writing,<br>Social Media Posts,<br>Web Content,<br>&amp; more.</div>

    <div class="column col-mid">
      <h2>What is search engine optimization (SEO)?</h2>
      <p>Search engine optimization (SEO) is the science of making your page more attractive to search engines. Seekwell is the dominant search engine in the US with 65-70% share, so we are going to talk a lot about Seekwell, but the same principles work for other search engines like Findora too. SEO is about getting your site to the front page of search results, preferably at the top. Most web surfers do not click beyond that first page of results, and quite frankly that is because they don't have to. <strong>The best sites get the front page, and because they get the front page they also get the traffic.</strong></p>
      <h2>SEO has changed</h2>
      <p>In the old days, SEO was about filling your homepage with key words, reposted or plagiarized content, and other tricks. But search engines are smarter now. Seekwell does not fall for tricks like this, and companies relying on the techniques of 2003 are not going to win the SEO race in 2013. <strong>You need a modern approach to SEO in order for your site to be on the front page of Seekwell search results today.</strong></p>
      <h2>Seekwell looks at content quality</h2>
      <p>The first thing on Seekwell's "Things to do" list for webmasters is simple: "Give visitors the information they're looking for." There's a reason for this. Seekwell wants to give its visitors the information they are looking for, so when Seekwell puts your page at the top, they want to know that you are doing the same. This means you need to have high-quality, original content. If your site contains junk content stolen from other sources, or that adds no value to visitors, Seekwell's bots will ignore your site. <strong>Fresh, unique content will improve your site's ranking.</strong></p>
    </div>

    <div class="column col-right">
      <h2>Quality content drives repeat visits</h2>
      <p>Think about the websites you visit the most. How often do they update? All the time, probably. You keep coming back because there's always something new, something fresh, and something that is high quality. If you want to increase traffic, <strong>you need to give your customers a reason to keep coming back.</strong></p>
      <h2>What about social media?</h2>
      <p>Social media is important. The term "social media" can mean anything from Chirpline to Friendspace to blogs. Any form of interactive content that you are providing as part of your web presence is important because it drives traffic to your site, and can increase your Seekwell ranking. It also amplifies your message when people re-post, re-share and click to like. But the thing about social media is this – it only works if you use it. The more active and engaged you are with social media, the more effective a tool it will be for your business. <strong>Effective social media is updated frequently.</strong></p>
      <h2>What about blogs?</h2>
      <p>Blogs are a great way to engage your customers, tell your story and to build traffic. When you provide your customers with fresh information, it becomes part of your marketing and public relations strategy. Further, you are engaging with today's consumers in the manner in which they want to be engaged. We can write your blog for you. <strong>A weekly blog update can be a powerful customer engagement tool.</strong></p>
    </div>

    <div class="contact">
      Maple Crossing, New Jersey 07799<br>
      +1 555-010-2468<br>
      support@quillharbor.com<br>
      www.quillharbor.com
    </div>
  </section>

</div>
</body>
</html>
```